Would need to a simple sticker for baby wipe. (Layout provided)

Hi guys,
I would need to design a removable sticker that located under the lid of baby wipe, please look at picture 1 then you will get what it is (the yellow oval). It just a sticker that consumer will removed at the beginning in order to take out the wipe.
-Picture 2 and 3: are some ideas from other competitors. As you could see, most are oval shapes, and the ideas are quite variety, some are very simple, some is more complicate.
-Picture 4: is my actual product.
-File "layout.AI" is where you could begin with (or not, if you want). I hope you could help to design a simple design, but still somehow match with the overall design of the product (which already have quite soft and colorful pastel).
Dimension is around 6x3 cm
The idea are totally freedom.
Thank you for your help

```html
<!DOCTYPE html>
<html lang="en">
<head>
<meta charset="utf-8">
<title>Baby Wipe Lid Sticker</title>
<link href="https://fonts.googleapis.com/css2?family=Montserrat:wght@500&display=swap" rel="stylesheet">
<style>
  :root {
    --pattern-light: #f9fafa;
    --pattern-blue: #d6e6ec;
    --pattern-sky: #dfe6f1;
    --pattern-sand: #ece3d4;
    --pattern-sage: #e2ebe6;
    --ring-teal: #43a1b6;
    --sticker-white: #ffffff;
    --sticker-tint: #e6f0f3;
    --dot-sand: #c7b596;
    --label-teal: #3aa2b8;
  }
  html, body {
    margin: 0;
    padding: 0;
    overflow: hidden;
  }
  .canvas {
    position: relative;
    width: 1200px;
    height: 587px;
    overflow: hidden;
    background: var(--pattern-light);
  }
  .pastel-pattern {
    position: absolute;
    inset: 0;
    background:
      radial-gradient(circle at 8% 18%, var(--pattern-blue) 0, transparent 14%),
      radial-gradient(circle at 17% 70%, var(--pattern-sky) 0, transparent 13%),
      radial-gradient(circle at 30% 10%, var(--pattern-sage) 0, transparent 12%),
      radial-gradient(circle at 50% 92%, var(--pattern-sand) 0, transparent 14%),
      radial-gradient(circle at 62% 8%, var(--pattern-sand) 0, transparent 12%),
      radial-gradient(circle at 80% 80%, var(--pattern-blue) 0, transparent 15%),
      radial-gradient(circle at 88% 25%, var(--pattern-sage) 0, transparent 13%),
      radial-gradient(circle at 95% 60%, var(--pattern-sand) 0, transparent 12%),
      radial-gradient(circle at 5% 92%, var(--pattern-sand) 0, transparent 12%),
      var(--pattern-light);
  }
  .sticker-art {
    position: absolute;
    inset: 0;
  }
  .open-label {
    font-family: "Montserrat", sans-serif;
    font-weight: 500;
    font-size: 11px;
    letter-spacing: 1px;
    fill: var(--label-teal);
  }
</style>
</head>
<body>
<div class="canvas">
  <div class="pastel-pattern" role="img" aria-label="Soft pastel pattern of fawns, butterflies, flowers, stars, hearts, bunnies and dots"></div>

  <svg class="sticker-art" width="1200" height="587" viewBox="0 0 1200 587">
    <defs>
      <filter id="sticker-shadow" x="-20%" y="-30%" width="140%" height="160%">
        <feDropShadow dx="0" dy="5" stdDeviation="6" flood-color="#5a6b70" flood-opacity="0.28"/>
      </filter>
      <path id="sticker-outline" d="M478 201 H694 C724 201 748 216 758 262 C772 262 786 274 786 291 C786 308 772 320 758 320 C748 360 724 376 694 376 H478 A54 54 0 0 1 424 322 V255 A54 54 0 0 1 478 201 Z"/>
      <clipPath id="sticker-clip"><use href="#sticker-outline"/></clipPath>
    </defs>

    <ellipse class="lid-ring" cx="590" cy="288" rx="288" ry="147" fill="none" stroke="var(--ring-teal)" stroke-width="28"/>

    <use class="peel-sticker" href="#sticker-outline" fill="var(--sticker-white)" filter="url(#sticker-shadow)"/>

    <g clip-path="url(#sticker-clip)">
      <rect class="peel-tint" x="686" y="195" width="110" height="190" fill="var(--sticker-tint)"/>
      <path class="pull-arrow" d="M580 285 L660 226 V256 H690 V314 H660 V344 Z" fill="var(--sticker-tint)"/>
    </g>

    <path class="perforation" d="M484 215 H660 A74 74 0 0 1 660 363 H484 A46 46 0 0 1 438 317 V261 A46 46 0 0 1 484 215 Z" fill="none" stroke="var(--dot-sand)" stroke-width="1.6" stroke-dasharray="1.5 4.5" stroke-linecap="round"/>

    <text class="open-label" transform="translate(747 289) rotate(90)" text-anchor="middle">OPEN</text>

    <g class="open-icon" fill="none" stroke="var(--label-teal)" stroke-width="2.6" stroke-linecap="round" stroke-linejoin="round">
      <path d="M764 288 A8 8 0 1 0 777 296"/>
      <path d="M778 290 V296.5 H771.5"/>
    </g>
  </svg>
</div>
</body>
</html>
```